Book Cover and Logo Design

We want a cover designed for a book titled, "The Open Harvest Blueprint" Subtitled "The Decade Program to Rebuild Society, Dissolve the Levy Maze, Clear the Public Ledger, and Revive the Shared Promise" and a logo that we can use on social media when talking about The Open Harvest Blueprint.

This book succeeds Mending Horizon, on the website https://www.mendinghorizon.example

You can see The Open Harvest Blueprint on the website. It gives American's basic income, free healthcare, and free college while slashing personal income taxes and paying off the national debt. The Tide Levy that would replace income taxes would also fund huge infrastructure projects like high speed mag lev trains criss-crossing the nation, a moon base, major desalinization projects to provide water for Western cities and farms.

Target Market(s)

American voters

Industry/Entity Type

American economic policy

Requirements
Must have
• the book cover should be exciting, portraying images of a futuristic America, but with nature tucked into the scenes too
Nice to have
• Patriotic colors
Should not have
• Nothing partisan at all

```html
<!DOCTYPE html>
<html lang="en">
<head>
<meta charset="utf-8">
<title>The Open Harvest Blueprint — Cover and Logo</title>
<link rel="stylesheet" href="https://fonts.googleapis.com/css2?family=Cinzel:wght@400;600;700&family=Barlow+Semi+Condensed:wght@600;700&display=swap">
<style>
  :root {
    --backdrop: #435163;
    --red: #c4161c;
    --navy: #13224a;
    --white: #ffffff;
    --space: #101a3a;
    --sky: #2f4577;
    --haze: #b9bfc9;
    --cream: #efe0c4;
    --glow: #f0c27c;
    --amber: #b07d3f;
    --olive: #4d4a2e;
    --forest: #26302a;
    --ground: #121616;
  }
  * { margin: 0; padding: 0; box-sizing: border-box; }
  html, body { width: 1200px; height: 1000px; overflow: hidden; }
  body { background: var(--backdrop); position: relative; font-family: "Cinzel", serif; }

  .cover {
    position: absolute; left: 130px; top: 152px; width: 488px; height: 690px;
    overflow: hidden; box-shadow: 0 10px 24px rgba(0,0,0,.45);
  }
  .cover-art {
    position: absolute; inset: 0;
    background:
      radial-gradient(ellipse 60% 38% at 18% 10%, rgba(30,44,112,.9), rgba(30,44,112,0) 72%),
      radial-gradient(ellipse 45% 16% at 14% 40%, rgba(190,55,65,.35), rgba(190,55,65,0) 72%),
      radial-gradient(ellipse 34% 20% at 80% 20%, rgba(175,170,165,.5), rgba(175,170,165,0) 72%),
      radial-gradient(circle at 32% 61%, rgba(255,240,180,.95) 0, rgba(246,192,98,.6) 12%, rgba(246,192,98,0) 34%),
      radial-gradient(ellipse 55% 22% at 88% 86%, rgba(60,120,140,.55), rgba(60,120,140,0) 72%),
      radial-gradient(ellipse 50% 24% at 8% 76%, rgba(48,70,34,.7), rgba(48,70,34,0) 72%),
      radial-gradient(ellipse 40% 16% at 92% 66%, rgba(70,110,50,.6), rgba(70,110,50,0) 72%),
      linear-gradient(180deg, var(--space) 0%, var(--sky) 14%, var(--haze) 32%, var(--cream) 46%, var(--glow) 58%, var(--amber) 66%, var(--olive) 76%, var(--forest) 88%, var(--ground) 100%);
  }

  .title-line { position: absolute; left: 0; right: 0; text-align: center; line-height: 1; font-weight: 600; }
  .title-the, .title-open { color: var(--white); text-shadow: 0 2px 6px rgba(0,0,0,.35); }
  .title-harvest { color: var(--red); font-weight: 700; }
  .title-blueprint { color: var(--navy); }

  .cover .title-the { top: 74px; font-size: 46px; }
  .cover .title-open { top: 118px; font-size: 56px; }
  .cover .title-harvest { top: 168px; font-size: 64px; }
  .cover .title-blueprint { top: 226px; font-size: 46px; }

  .star-rule { position: absolute; left: 50%; transform: translateX(-50%); }

  .subtitle {
    position: absolute; left: 50%; transform: translateX(-50%);
    text-align: center; color: var(--navy);
    font-family: "Barlow Semi Condensed", sans-serif; font-weight: 700;
    text-transform: uppercase;
  }
  .cover .subtitle { top: 330px; width: 340px; font-size: 13.5px; line-height: 16.5px; }

  .values {
    position: absolute; left: 0; right: 0; top: 634px;
    display: flex; justify-content: center; align-items: center; gap: 12px;
    color: var(--white); font-size: 15px;
  }
  .values .sep { color: var(--red); font-size: 14px; }
  .base-stars { position: absolute; left: 86px; top: 655px; }

  .logo { position: absolute; left: 745px; top: 350px; width: 318px; height: 300px; }
  .logo .title-the { top: 12px; font-size: 40px; text-shadow: none; }
  .logo .title-open { top: 52px; font-size: 48px; text-shadow: none; }
  .logo .title-harvest { top: 99px; font-size: 58px; }
  .logo .title-blueprint { top: 156px; font-size: 42px; }
  .logo .star-rule { top: 200px; }
  .logo .subtitle { top: 241px; width: 318px; font-size: 12.5px; line-height: 15.5px; }
</style>
</head>
<body>

<section class="cover">
  <div class="cover-art" role="img" aria-label="Futuristic American landscape: waving flag and moon base in a starry sky, domed capitol at sunrise, city skyline, maglev train on a viaduct, desalination pools, wind turbines and green hills"></div>

  <h1>
    <span class="title-line title-the">THE</span>
    <span class="title-line title-open">OPEN</span>
    <span class="title-line title-harvest">HARVEST</span>
    <span class="title-line title-blueprint">BLUEPRINT</span>
  </h1>

  <svg class="star-rule" style="top:284px" width="332" height="34" viewBox="0 0 332 34" aria-hidden="true">
    <line x1="0" y1="18" x2="332" y2="18" stroke="var(--red)" stroke-width="2"/>
    <polygon points="166,2 170.3,13.5 182,13.5 172.5,20.5 176,32 166,25 156,32 159.5,20.5 150,13.5 161.7,13.5" fill="var(--red)"/>
  </svg>

  <p class="subtitle">The Decade Program to Rebuild Society, Dissolve the Levy Maze, Clear the Public Ledger, and Revive the Shared Promise</p>

  <div class="values">
    <span>FREEDOM</span><span class="sep">★</span><span>PROSPERITY</span><span class="sep">★</span><span>OPPORTUNITY</span>
  </div>

  <svg class="base-stars" width="316" height="16" viewBox="0 0 316 16" aria-hidden="true">
    <line x1="0" y1="8" x2="114" y2="8" stroke="var(--red)" stroke-width="1.5"/>
    <line x1="202" y1="8" x2="316" y2="8" stroke="var(--red)" stroke-width="1.5"/>
    <g fill="var(--white)" font-size="12" font-family="serif" text-anchor="middle">
      <text x="125" y="13">★</text><text x="149" y="13">★</text><text x="172" y="13">★</text><text x="196" y="13">★</text>
    </g>
  </svg>
</section>

<section class="logo" aria-label="The Open Harvest Blueprint logo">
  <div class="title-line title-the">THE</div>
  <div class="title-line title-open">OPEN</div>
  <div class="title-line title-harvest">HARVEST</div>
  <div class="title-line title-blueprint">BLUEPRINT</div>

  <svg class="star-rule" width="312" height="32" viewBox="0 0 312 32" aria-hidden="true">
    <line x1="0" y1="17" x2="312" y2="17" stroke="var(--red)" stroke-width="2"/>
    <polygon points="156,2 160,13 171,13 162,19.5 165.5,30 156,23.5 146.5,30 150,19.5 141,13 152,13" fill="var(--red)"/>
  </svg>

  <p class="subtitle">The Decade Program to Rebuild Society, Dissolve the Levy Maze, Clear the Public Ledger, and Revive the Shared Promise</p>
</section>

</body>
</html>
```